Logo and business card for optometric practice
Calvin Mortenhall & Associates
Petra Valunkova, O.D.
Simon Orchardt, O.D.
Neil Tabarrou, O.D.
417 Meadowbrook Parkway
Ashfield Terrace, New York 11498
516-555-0142

Target Market(s)

Patients, general public

Industry/Entity Type

Business

Logo Text

Calvin Mortenhall & Associates Optometrists

Logo styles of interest
Pictorial/Combination Logo
Font styles to use
Serif
Sans Serif

Requirements
Must have
• current inspiration: realistic or photo closeup of eye, with interesting treatment of the iris OR
tech look, with closeup of eye and grid like the doctor is looking through a camera or microscope to view the eye up close
Should not have
• NO cartoons

```html
<!DOCTYPE html>
<html lang="en">
<head>
<meta charset="utf-8">
<title>Calvin Mortenhall &amp; Associates — Business Card</title>
<link rel="stylesheet" href="https://fonts.googleapis.com/css2?family=Jost:wght@400;500;700&display=swap">
<style>
  :root {
    --page-bg: #eeeeee;
    --card-black: #050505;
    --card-sheen: #1c1c1c;
    --white: #ffffff;
    --brand-blue: #2e4a8e;
    --bright-blue: #4a8fd0;
    --name-blue: #3f86c8;
  }
  * { box-sizing: border-box; margin: 0; padding: 0; }
  html, body { width: 1200px; height: 1000px; overflow: hidden; }
  body {
    background: radial-gradient(ellipse at center, #ffffff 0%, var(--page-bg) 100%);
    font-family: "Jost", sans-serif;
    color: var(--white);
    position: relative;
  }
  .card {
    position: absolute;
    width: 660px;
    height: 390px;
    background: radial-gradient(ellipse at 50% 30%, var(--card-sheen) 0%, var(--card-black) 70%);
    overflow: hidden;
  }
  .card-front { left: 90px; top: 110px; }
  .card-back { left: 450px; top: 530px; }

  .front-swoosh { position: absolute; inset: 0; width: 100%; height: 100%; }

  .brand {
    position: absolute;
    display: flex;
    flex-direction: column;
    align-items: center;
    font-weight: 500;
    color: var(--white);
    text-transform: uppercase;
  }
  .brand-dot {
    border-radius: 50%;
    background: var(--bright-blue);
  }
  .card-front .brand { left: 0; right: 0; top: 78px; }
  .card-front .brand-dot { width: 64px; height: 64px; margin-bottom: 36px; }
  .card-front .brand-name { font-size: 44px; line-height: 1; letter-spacing: 0.5px; }
  .card-front .brand-sub { font-size: 20px; letter-spacing: 9px; margin-top: 6px; }

  .card-back .brand { left: 20px; width: 290px; top: 90px; }
  .card-back .brand-dot { width: 50px; height: 50px; margin-bottom: 34px; }
  .card-back .brand-name { font-size: 24px; line-height: 1; white-space: nowrap; }
  .card-back .brand-sub { font-size: 11px; letter-spacing: 5px; margin-top: 4px; }

  .divider {
    position: absolute;
    left: 335px;
    top: 28px;
    width: 2px;
    height: 300px;
    background: var(--white);
  }
  .contact {
    position: absolute;
    left: 385px;
    top: 62px;
    font-size: 17px;
    line-height: 21px;
    font-weight: 400;
  }
  .contact-name {
    color: var(--name-blue);
    font-weight: 700;
    font-size: 22px;
    margin: 0 0 26px 10px;
    white-space: nowrap;
  }
  .contact-lines { list-style: none; margin-bottom: 22px; }
  .contact-lines .label { display: inline-block; width: 16px; margin-left: 6px; }
  .contact address { font-style: normal; }
</style>
</head>
<body>

  <section class="card card-front" aria-label="Business card front">
    <svg class="front-swoosh" viewBox="0 0 660 390" preserveAspectRatio="none" aria-hidden="true">
      <defs>
        <linearGradient id="swooshBlue" x1="0" y1="0" x2="1" y2="0">
          <stop offset="0" stop-color="#2e4a8e"/>
          <stop offset="0.55" stop-color="#4a8fd0"/>
          <stop offset="1" stop-color="#2e4a8e"/>
        </linearGradient>
      </defs>
      <path d="M0 352 Q 420 350 660 240 L660 390 L0 390 Z" fill="url(#swooshBlue)"/>
      <path d="M0 344 Q 420 342 660 232" fill="none" stroke="#ffffff" stroke-width="6"/>
    </svg>
    <div class="brand">
      <span class="brand-dot" aria-hidden="true"></span>
      <span class="brand-name">Calvin Mortenhall</span>
      <span class="brand-sub">&amp; Associates</span>
    </div>
  </section>

  <section class="card card-back" aria-label="Business card back">
    <div class="brand">
      <span class="brand-dot" aria-hidden="true"></span>
      <span class="brand-name">Calvin Mortenhall</span>
      <span class="brand-sub">&amp; Associates</span>
    </div>
    <span class="divider" aria-hidden="true"></span>
    <div class="contact">
      <p class="contact-name">Petra Valunkova, O.D.</p>
      <ul class="contact-lines">
        <li><span class="label">T</span>516-555-0142</li>
        <li><span class="label">F</span>516-555-0187</li>
        <li>office@mortenhalleye.com</li>
      </ul>
      <address>
        417 Meadowbrook Parkway<br>
        Ashfield Terrace,<br>
        NY 11498
      </address>
    </div>
  </section>

</body>
</html>
```